HIDE WARDEN

Labels for Men's Skin Care. Organic, target 25-35 The label will be 2x3.5 on a 4oz amber bottle. 3 labels with the information shown on the uploaded sample.
Our product is a e-commerce built to help my 24 year old twin sons have a business of their own. Although it will be sold online they will also do foot work and sell to barbers at barber shops using as a mist on customers after shaving. So we want something that will attract male customers and will look good in a modern Barbershop. This is there shot and packaging is very very important. So if you could help us out with a great label we would be working with you in the future for package design. Our line will have several mens Organic natural skin care cleanser, mask toners and moisturizers..Thank you for your help. We also hope to put our products in beauty supply shops. So it needs to stand out as a mans product but still be traditional male product. Oh be creative mind that you are and remember we are trying to build a brand that attracts 25-35 male. Thank you

Hello, I just wanted to let you know that I am up working very late.

for anyone on the other side of the world up and working. I sleep about
3 hours.. So I'll be up for a few more hours and then up again around 5am my time

Good morning... I just wanted to say I will need three labels.. The words on all three are not that different and will fit pretty much the same on all three. So if you could work with one showing how the colors might be a little different on the other two you can do that with just the one label Just to make it easier on you if you like.. we can fix the other two once I find the right label,  Thank you it is 3am here.. still working.. I love it.

Target Market(s)

MALE 25-35

Industry/Entity Type

E-Commerce

Requirements
Must have
• final design must be fitted to the dieline uploaded.

```html
<!DOCTYPE html>
<html lang="en">
<head>
<meta charset="utf-8">
<title>Hide Warden for Men – Smooth Skin Blend Label</title>
<link rel="stylesheet" href="https://fonts.googleapis.com/css2?family=Orbitron:wght@700;800&family=Lato:wght@400;700&display=swap">
<style>
  :root {
    --page: #ffffff;
    --backdrop-top: #e8801c;
    --backdrop-bottom: #9e2329;
    --band: #6e4527;
    --dieline: #3a2418;
    --tree-light: #9ccf6a;
    --tree-dark: #4f8f3a;
  }
  html, body {
    margin: 0;
    width: 1200px;
    height: 1200px;
    overflow: hidden;
    background: var(--page);
  }
  .artboard { display: block; width: 1200px; height: 1200px; }

  /* label themes passed into the shared label symbol */
  .label--amber {
    --label-bg: rgba(120, 40, 20, 0.16);
    --brand: #ffffff;
    --text: #ffffff;
    --side: #ffffff;
  }
  .label--stone {
    --label-bg: #e8e4df;
    --brand: #c2602c;
    --text: #ffffff;
    --side: #ffffff;
  }

  .label-bg { fill: var(--label-bg); }
  .brand-name {
    font-family: "Orbitron", sans-serif;
    font-weight: 800;
    fill: var(--brand);
    letter-spacing: 2px;
  }
  .blend-band { fill: var(--band); }
  .blend-name {
    font-family: "Orbitron", sans-serif;
    font-weight: 700;
    font-size: 26px;
    fill: #ffffff;
    letter-spacing: 2px;
  }
  .blend-type {
    font-family: "Lato", sans-serif;
    font-size: 27px;
    fill: #ffffff;
  }
  .side-tag {
    font-family: "Lato", sans-serif;
    font-size: 23px;
    fill: var(--side);
  }
  .benefit {
    font-family: "Lato", sans-serif;
    font-weight: 700;
    font-size: 35px;
    fill: var(--text);
  }
  .scent {
    font-family: "Lato", sans-serif;
    font-size: 28px;
    fill: var(--text);
  }
  .volume {
    font-family: "Orbitron", sans-serif;
    font-weight: 700;
    font-size: 22px;
    fill: var(--text);
    letter-spacing: 2px;
  }
  .dieline {
    fill: none;
    stroke: var(--dieline);
    stroke-width: 1.5;
    stroke-dasharray: 12 8;
  }
</style>
</head>
<body>
<svg class="artboard" viewBox="0 0 1200 1200" xmlns="http://www.w3.org/2000/svg">
  <defs>
    <linearGradient id="backdrop-gradient" x1="0" y1="0" x2="0" y2="1">
      <stop offset="0" stop-color="var(--backdrop-top)"/>
      <stop offset="1" stop-color="var(--backdrop-bottom)"/>
    </linearGradient>
    <linearGradient id="tree-gradient" x1="0" y1="0" x2="0" y2="1">
      <stop offset="0" stop-color="var(--tree-light)"/>
      <stop offset="1" stop-color="var(--tree-dark)"/>
    </linearGradient>

    <symbol id="smooth-skin-label" viewBox="0 0 545 965">
      <rect class="label-bg" x="0" y="0" width="545" height="965" rx="26"/>

      <rect x="66" y="12" width="414" height="262" rx="120" fill="url(#tree-gradient)"
            role="img" aria-label="Illustration of a broad green oak tree on a patch of grass"/>

      <text class="brand-name" x="272" y="454" text-anchor="middle" font-size="50" transform="translate(0 -131)">HIDE WARDEN</text>
      <text class="brand-name" x="272" y="395" text-anchor="middle" font-size="50">FOR MEN</text>

      <rect class="blend-band" x="0" y="466" width="545" height="125"/>
      <text class="blend-name" x="272" y="520" text-anchor="middle">SMOOTH SKIN BLEND</text>
      <text class="blend-type" x="272" y="566" text-anchor="middle">Botanical Healing Mist</text>

      <text class="side-tag" x="0" y="0" text-anchor="middle" transform="translate(36 718) rotate(-90)">Daily Shave FIX</text>

      <text class="benefit" x="86" y="643">Facial Conditioner +</text>
      <text class="benefit" x="86" y="721">Calms Razor Burn</text>
      <text class="benefit" x="86" y="800">After Shaving</text>

      <text class="scent" x="272" y="882" text-anchor="middle">Cranberry + Pomegranate</text>
      <text class="volume" x="272" y="925" text-anchor="middle">3.5 FL OZ 103ML</text>
    </symbol>
  </defs>

  <!-- small stone colourway -->
  <use class="label--stone" href="#smooth-skin-label" x="0" y="459" width="325" height="575"/>

  <!-- presentation backdrop with amber colourway -->
  <rect x="410" y="0" width="790" height="1200" fill="url(#backdrop-gradient)"/>
  <rect class="dieline" x="497" y="93" width="580" height="1011" rx="40"/>
  <use class="label--amber" href="#smooth-skin-label" x="515" y="110" width="545" height="965"/>
</svg>
</body>
</html>
```